Web Design Project

need a website, logo and a matching business Card for design studio. i have a company that works with many companies and i want to offer design services that will be outsourced to craftflock.

this website is totally for the design services. i need it to be simple but very catcgy and trendy, yet MUST BE ELEGENT.

you being a designer will know best what do i require in this website and how it should look and feel..

i dont need many pages, most of the selling work to clients will be face to face, this is just for them to view the sample works.

the company is called "Corvelin, Vividra Studio", so pages i need are: 1- the Studio 2- Folios 3- Contact us( will include company informaiton, and online contact form that should have a drop-down list of all types of designs.

main focus is the folios pages, it needs to have samples of works, the classification of works should be on two basis, by type of design and by designer. client should be able to select a certain designer and send an inquiry. if the customer does that, then i should get all client details and the designer should get a notification that he has been requested though no contact details of client should be given to designer as i want to make sure that those jobs are given to designer through craft flock and this is an invitation for any designer who care to put his works on the website. next to that, if the customer requires a job online then we need to get information on how design should feel and look.

please quote your price to include the website and business card design, A3 head letter and envelope.

Please provide a mock up of your design or a briefing an initial design before asking to be announced as the winner.

my customers are general managers and decision makers.

Business

• ability to filiter works based on type or designer. and website must offer all types of designs included here

```html
<!DOCTYPE html>
<html lang="en">
<head>
<meta charset="utf-8">
<title>Corvelin Vividra Studio</title>
<link rel="stylesheet" href="https://fonts.googleapis.com/css2?family=Pinyon+Script&family=Italianno&display=swap">
<style>
  :root {
    --paper: #ffffff;
    --brand-red: #c23a1e;
    --tagline-grey: #6f6f6f;
    --button-ink: #111111;
    --silver-light: #f4f4f4;
    --silver-mid: #c9c9c9;
    --silver-dark: #8c8c8c;
    --tone-green: #8fbf45;
    --tone-blue: #3f6fc0;
    --tone-sky: #7fc2ea;
    --tone-orange: #f0a040;
  }
  * { margin: 0; padding: 0; box-sizing: border-box; }
  html, body { width: 1200px; height: 862px; overflow: hidden; background: var(--paper); }
  .canvas { position: relative; width: 1200px; height: 862px; overflow: hidden; background: var(--paper); }
  .backdrop {
    position: absolute; inset: 0;
    background:
      radial-gradient(ellipse 560px 420px at 0% 0%, rgba(63,111,192,0.75), rgba(143,191,69,0.45) 55%, rgba(255,255,255,0) 100%),
      radial-gradient(ellipse 900px 640px at 100% 100%, var(--tone-blue), rgba(127,194,234,0.7) 40%, rgba(240,160,64,0.45) 62%, rgba(143,191,69,0.25) 78%, rgba(255,255,255,0) 100%),
      var(--paper);
  }
  .welcome-panel {
    position: absolute; left: 241px; top: 254px; width: 729px; height: 334px;
    background: rgba(255,255,255,0.72);
    border: 1px solid rgba(255,255,255,0.9);
    border-radius: 7px;
    box-shadow: 0 0 18px rgba(180,200,220,0.45);
  }
  .brand-dot {
    position: absolute; left: 60px; top: 56px;
    width: 34px; height: 34px; border-radius: 50%; background: var(--brand-red);
  }
  .brand-name {
    position: absolute; left: 150px; top: 30px;
    font-family: "Pinyon Script", cursive; font-size: 68px; font-weight: 400;
    color: var(--brand-red); line-height: 1; white-space: nowrap;
  }
  .tagline {
    position: absolute; left: 177px; top: 132px;
    font-family: "Italianno", cursive; font-size: 38px; color: var(--tagline-grey);
    letter-spacing: 0.5px; line-height: 1; white-space: nowrap;
  }
  .enter-button {
    position: absolute; left: 321px; top: 231px; width: 210px; height: 50px;
    border-radius: 25px; border: 2px solid var(--silver-dark);
    background: linear-gradient(to bottom, var(--silver-light) 0%, #e2e2e2 45%, var(--silver-mid) 55%, #e9e9e9 100%);
    box-shadow: inset 0 0 0 3px rgba(255,255,255,0.8), 0 2px 4px rgba(0,0,0,0.25);
    display: flex; align-items: center; justify-content: center;
    font-family: "Pinyon Script", cursive; font-size: 34px; color: var(--button-ink);
    text-decoration: none;
  }
  .enter-button-reflection {
    position: absolute; left: 321px; top: 284px; width: 210px; height: 36px;
    border-radius: 25px 25px 0 0;
    background: linear-gradient(to bottom, rgba(170,170,170,0.35), rgba(255,255,255,0));
  }
</style>
</head>
<body>
<main class="canvas">
  <div class="backdrop" role="img" aria-label="Abstract flowing ribbon artwork in green, blue, orange and pink sweeping across the corners"></div>

  <section class="welcome-panel">
    <span class="brand-dot"></span>
    <span class="brand-name">Corvelin Vividra studio</span>
    <p class="tagline">personify your business</p>
    <a class="enter-button" href="#">Click Here</a>
    <div class="enter-button-reflection"></div>
  </section>
</main>
</body>
</html>
```